Book cover for New Book: Whispers Beneath Red Rock. Top of the cover-Corwin Ashby
Title:Whispers Beneath Red Rock
subtitle: Sometimes the past is best left buried
Author name: M. K. Brandvold
Picturing the background to be a piture of Monument Valley, Az. with stormy clouds-maybe a lightning bolt, and long shadows.
Need coverwith spine and blurb, front cover 2x2 pisture, Design must mee all Zephora and Listenry requirements. Cover 2500 H,1600W. 300DPI. Jpeg. 24 bit color, RGB.

```html
<!DOCTYPE html>
<html lang="en">
<head>
<meta charset="utf-8">
<title>Whispers Beneath Red Rock — Cover</title>
<link rel="stylesheet" href="https://fonts.googleapis.com/css2?family=Big+Shoulders+Stencil+Display:wght@800;900&family=Oswald:wght@400;500;600&display=swap">
<style>
  :root {
    --page-bg: #ececec;
    --sky-violet: #3b2440;
    --sky-rose: #b98a9a;
    --sky-glow: #d9b8a8;
    --mesa-red: #8a3a2a;
    --desert-orange: #b4582a;
    --desert-rust: #7a3a1e;
    --ground-brown: #4a2a1a;
    --ground-dark: #2a1a12;
    --ink-white: #f1ede6;
    --ink-soft: #e2d6cb;
    --ink-blue: #7d9cc4;
  }
  * { margin: 0; padding: 0; box-sizing: border-box; }
  html, body {
    width: 1200px; height: 1200px; overflow: hidden;
    background: var(--page-bg);
  }
  .cover {
    position: absolute;
    left: 255px; top: 48px;
    width: 690px; height: 1104px;
    overflow: hidden;
    box-shadow: 0 6px 24px rgba(0,0,0,0.25);
  }
  .cover-art {
    position: absolute; inset: 0;
    background:
      radial-gradient(ellipse 70% 22% at 50% 28%, rgba(217,184,168,0.55), transparent 70%),
      linear-gradient(180deg,
        var(--sky-violet) 0%,
        #6a4660 10%,
        var(--sky-rose) 24%,
        var(--sky-glow) 32%,
        #9a6a78 40%,
        var(--mesa-red) 46%,
        var(--desert-orange) 52%,
        var(--desert-rust) 62%,
        var(--ground-brown) 74%,
        var(--ground-dark) 100%);
  }
  .series-name {
    position: absolute; top: 60px; left: 0; right: 0;
    text-align: center;
    font-family: "Oswald", sans-serif; font-weight: 500;
    font-size: 42px; letter-spacing: 0.22em;
    color: var(--ink-white);
  }
  .title {
    position: absolute; top: 570px; left: 40px; right: 40px;
    text-align: center;
    font-family: "Big Shoulders Stencil Display", sans-serif; font-weight: 900;
    text-transform: uppercase;
    line-height: 0.95;
  }
  .title-main {
    display: block; font-size: 150px; color: var(--ink-white);
  }
  .title-link {
    display: block; font-size: 56px; font-weight: 800; color: var(--ink-white);
    margin: 6px 0 4px;
  }
  .title-end {
    display: block; font-size: 150px; color: var(--ink-blue);
  }
  .subtitle {
    position: absolute; top: 948px; left: 60px; right: 60px;
    text-align: center;
    font-family: "Oswald", sans-serif; font-weight: 400;
    font-size: 22px; letter-spacing: 0.06em;
    color: var(--ink-soft);
  }
  .author {
    position: absolute; bottom: 46px; left: 0; right: 0;
    text-align: center;
    font-family: "Oswald", sans-serif; font-weight: 600;
    font-size: 36px; letter-spacing: 0.24em;
    color: var(--ink-white);
  }
</style>
</head>
<body>
  <div class="cover">
    <div class="cover-art" role="img" aria-label="Photograph of Monument Valley mesas under a stormy violet sky with lightning, a lone figure walking down a straight desert highway casting a long shadow"></div>
    <div class="series-name">CORWIN ASHBY</div>
    <h1 class="title">
      <span class="title-main">Whispers</span>
      <span class="title-link">Beneath</span>
      <span class="title-end">Red Rock</span>
    </h1>
    <p class="subtitle">Sometimes the past is best left buried</p>
    <div class="author">M. K. BRANDVOLD</div>
  </div>
</body>
</html>
```